Cruise Booking Website

Cruise search and booking website

This project is a redesign of a cruise booking website we did a few years ago.

The current website is located here: http://voyage.pixelmarsh.com/en/

It's not fully functional but gives you ad idea how miserable the old design was.

All the information about cruises, cruise lines, destinations, ports and shore excursions will be similar to http://www.sailorbay.com/
Actual search pages (form, results, single result, sailing and cabin selection, ship info, booking) will have EXACTLY the same info as sailorbay.com

We like the style of http://harborvoyagehub.com, it's quite modern, good spacing, not overloaded with information. So you can use it as an example of what we like, not what we want as a final result for us. Please, don't copy it. The result should not be possible to resemble the harborvoyagehub.com, because our site has to be unique. This is important!
If you submit a design that clearly reminds another cruise site it will be rejected!

Also the mockup provided is just to give you the basic structure and show what information has to be present on the page. It doesn't mean the layout has to be the same as a mockup. The layout is up to the designer.

I've updated the mockup to be more generic so it doesn't confuse you:
https://www.filecrate.net/s/k7q2mz9pw4tnb3x/Home%20page.png

When you're adding social sharing icons like chatterbox/peeplet you have to use chinese ones instead:
https://www.filecrate.net/s/h3rt8wyd6jcl0fe/chinese-social-icons.png
Originals: http://shrtlk.example/qRmT

We'll start with home page first and after it's approved inner pages can be designed.

I know the cost of the project doesn't look high, but the task is straight forward and doesn't require to be very original, it's better to follow existing design and layout patterns that proved to work well.
That's why I encourage you to choose a template to build the design on top of one of https://themequarry.net/ themes if it will save the design work, will be easier and faster for you. So it will be more like a customization than a new design from scratch.

Mockups, site map and logo files:
- https://www.filecrate.net/sh/50xb7vq1ndtpkez/RmwuHp8Zq3

Website tree:
- https://papers.quillnet.example/document/d/8vTrXk2MqLpZ4wNsB7yHcE1oUjFgD9aR_QbVtnWm/edit?usp=sharing
Updates

So far a lot of designs are just copying http://www.harborvoyagehub.com/ - we don't like it!

We like the style of harborvoyagehub.com, it's quite modern, good spacing, not overloaded with information. So you can use it as an example of what we like, not what we want as a final result for us. Please, don't copy it. The result should not be possible to resemble the harborvoyagehub.com, because our site has to be unique. This is important!

Target Market(s)

Chinese travellers

Industry/Entity Type

Build

Requirements
Must have
• * White, blue and red
* Large spacing, not too much information cramped into a small space like sailorbay.com or the current website
* More "hidden" info in popups, tabs and so on, so not to many things are visible at the same time
* Compatible with lumen framekit styling (for easier coding):
- http://lumenkit.example.io/framework/index.html
- http://skinvault.net/
* Feel free to propose to build the design on top of one of https://themequarry.net/ themes if it will save the design work, will be easier and faster for you

```html
<!DOCTYPE html>
<html lang="en">
<head>
<meta charset="utf-8">
<title>Wavecrest – Destinations</title>
<link href="https://fonts.googleapis.com/css2?family=Lato:wght@300;400;700&display=swap" rel="stylesheet">
<style>
:root{
  --blue:#1e98cf;
  --blue-dark:#0b74b5;
  --blue-deep:#0a6aa6;
  --red:#c9362b;
  --grey-bg:#e4e4e4;
  --map-land:#5f5f5f;
  --text:#555;
  --text-dark:#333;
  --line:#c9c9c9;
  --white:#fff;
}
*{box-sizing:border-box;margin:0;padding:0}
html,body{width:694px;height:1200px;overflow:hidden;background:var(--white)}
body{position:relative;font-family:'Lato',sans-serif;color:var(--text);font-size:9px}
.abs{position:absolute}
a{color:inherit;text-decoration:none}

/* header */
.account{top:14px;right:31px;display:flex;align-items:center;gap:10px;font-size:8.5px}
.account .register{color:var(--blue-dark)}
.account .login{background:var(--blue-dark);color:var(--white);font-weight:700;padding:5px 8px}
.brand{top:32px;left:32px;display:flex;align-items:center;gap:8px;color:var(--blue-dark);font-weight:700;font-size:30px;letter-spacing:-.5px}
.brand .mark{width:34px;height:34px;border-radius:50%;background:var(--blue)}
.social{top:50px;left:523px;display:flex;gap:4px}
.social span{width:20px;height:20px;border-radius:3px;background:#9cc7e0}

.main-nav{top:94px;left:32px;display:flex;align-items:center;font-size:10px;color:var(--text-dark)}
.main-nav a{padding:4px 9px;margin-right:4px}
.main-nav a.current{background:var(--blue-dark);color:var(--white);padding:4px 7px}
.site-search{top:94px;left:543px;width:120px;height:20px;border:1px solid var(--line);font-size:9px;font-style:italic;color:#999;padding:4px 6px}
.site-search svg{position:absolute;right:5px;top:4px}

/* search band */
.search-band{top:124px;left:0;width:694px;height:90px}
.search-title{top:144px;left:31px;color:var(--white);font-size:13px;font-weight:300}
.select{top:170px;height:24px;background:var(--white);border:1px solid var(--line);font-size:8.5px;font-style:italic;color:#666;padding:7px 8px}
.select:after{content:"";position:absolute;right:8px;top:10px;border:3.5px solid transparent;border-top:4px solid #555}
.btn{top:170px;height:24px;color:var(--white);text-align:center;line-height:24px}
.btn.advanced{left:479px;width:89px;background:#9a9a9a;font-size:8.5px}
.btn.search{left:574px;width:69px;background:var(--red);font-weight:700;font-size:10.5px}

.breadcrumb{top:232px;left:32px;font-size:8px}
.breadcrumb b{color:var(--blue-dark)}

.page-title{top:262px;left:32px;font-size:23px;font-weight:300;color:var(--text)}
.world-map{top:299px;left:0;width:486px;height:251px;background:var(--grey-bg)}

.deals-title{top:276px;left:505px;font-size:8px;font-weight:700;letter-spacing:.5px;color:var(--text)}
.deal{left:505px;width:158px;height:74px}
.deal .caption{position:absolute;left:6px;right:6px;bottom:-3px;height:23px;background:var(--white);border-bottom:2px solid #d5d5d5;display:flex;justify-content:space-between;align-items:center;padding:0 6px;font-size:9.5px;color:var(--text-dark)}
.deal .price{color:var(--blue-dark);font-weight:700}

/* region */
.region-title{top:588px;left:31px;font-size:19px;color:var(--blue)}
.countries{top:628px;left:32px;display:grid;grid-template-columns:91px 91px 100px;row-gap:7px;font-size:8.5px}
.countries .active{color:var(--blue)}
.details{top:611px;left:354px;width:309px;height:171px;background:var(--grey-bg);border-top:1px solid var(--blue);border-bottom:2px solid #d2d2d2;padding:15px 19px}
.details h3{font-size:10.5px;font-weight:400;color:var(--text-dark);margin-bottom:19px}
.details p{font-size:9.3px;font-weight:300;line-height:19px;color:var(--text)}

/* partners */
.partners-title{top:815px;left:31px;font-size:11px;color:var(--text-dark);letter-spacing:.3px}
.partner{top:844px;width:88px;height:57px;border:1px solid var(--line);display:flex;align-items:center;justify-content:center}
.partner span{width:48px;height:14px;background:#d7dfe6;border-radius:2px}
.partner .round{width:22px;height:22px;border-radius:50%}
.arrow{top:865px;width:12px;height:12px;border-radius:50%}

/* footer */
.footer-bg{top:940px;left:0;width:694px;height:260px}
.footer-col{top:1000px;color:var(--white)}
.footer-col h4{font-size:11.5px;font-weight:700;margin-bottom:4px}
.footer-col li{list-style:none;font-size:7.5px;line-height:13.2px;padding-left:3px}
.footer-col li.current{text-decoration:underline;font-weight:700}
.footer-col p{font-size:7.5px;line-height:15px}
.news-input{width:101px;height:19px;background:var(--white);color:#777;font-size:7px;padding:5px 6px;margin:6px 0 8px}
.news-btn{display:inline-block;background:var(--red);color:var(--white);font-size:7.5px;font-weight:700;padding:4px 6px}
.contact-line{display:flex;align-items:flex-start;gap:7px}
.footer-brand{top:1126px;left:50px;display:flex;align-items:center;gap:7px;color:var(--white);font-weight:700;font-size:24px}
.footer-brand .mark{width:28px;height:28px;border-radius:50%;background:#8fd0ef}
.tagline{top:1168px;left:50px;color:var(--white);font-size:8px}
.copyright{top:1168px;right:50px;color:var(--white);font-size:7px;font-weight:700}
</style>
</head>
<body>

<header>
  <div class="abs account">
    <a class="register" href="#"><svg width="10" height="8" viewBox="0 0 10 8"><circle cx="4" cy="2.2" r="2" fill="#0b74b5"/><path d="M0 8c0-3 2-4 4-4s4 1 4 4z" fill="#0b74b5"/><path d="M8 1v3M6.5 2.5h3" stroke="#0b74b5"/></svg> Register</a>
    <a class="login" href="#">Log In</a>
  </div>
  <a class="abs brand" href="#"><span class="mark"></span>Wavecrest</a>
  <div class="abs social"><span></span><span></span><span></span><span></span><span></span><span></span></div>

  <nav class="abs main-nav">
    <a href="#">Home</a>
    <a class="current" href="#">Destinations ▾</a>
    <a href="#">Cruise lines</a>
    <a href="#">Cruise info</a>
    <a href="#">Deals</a>
    <a href="#">Online Booking</a>
    <a href="#">Contact Us</a>
  </nav>
  <div class="abs site-search">SEARCH
    <svg width="11" height="11" viewBox="0 0 11 11"><circle cx="4.5" cy="4.5" r="3.5" stroke="#555" stroke-width="1.5" fill="none"/><path d="M7 7l3.3 3.3" stroke="#555" stroke-width="1.8"/></svg>
  </div>
</header>

<section class="search-cruises">
  <svg class="abs search-band" viewBox="0 0 694 90" preserveAspectRatio="none">
    <rect width="694" height="90" fill="#1e98cf"/>
    <path d="M0 0H694V4C620 12 540 2 440 6S250 12 160 6 40 4 0 8Z" fill="#fff"/>
  </svg>
  <div class="abs search-title">Search cruises</div>
  <div class="abs select" style="left:32px;width:99px">Destination</div>
  <div class="abs select" style="left:139px;width:99px">Date</div>
  <div class="abs select" style="left:246px;width:100px">Length</div>
  <div class="abs select" style="left:354px;width:100px">Cruise line</div>
  <div class="abs btn advanced">Advanced search</div>
  <div class="abs btn search">Search</div>
</section>

<div class="abs breadcrumb">Home &gt; <b>Destinations</b></div>

<main>
  <h1 class="abs page-title">Explore the world</h1>
  <div class="abs world-map" role="img" aria-label="World map with South America highlighted in blue"></div>

  <h2 class="abs deals-title">LAST MINUTE DEALS</h2>
  <div class="abs deal" style="top:299px;background:linear-gradient(160deg,#8a3a8e,#b2487c 45%,#6b3a2a)" role="img" aria-label="Cruise ship pool deck at dusk">
    <div class="caption"><span>Bahamas - 5 days</span><span class="price">$1200</span></div>
  </div>
  <div class="abs deal" style="top:388px;background:linear-gradient(180deg,#3a64b0,#2a4d9a 60%,#1f3f86)" role="img" aria-label="White yacht on blue sea">
    <div class="caption"><span>Bahamas - 5 days</span><span class="price">$1200</span></div>
  </div>
  <div class="abs deal" style="top:477px;background:linear-gradient(180deg,#b9c6cf,#5c6f4c 45%,#3d4a36)" role="img" aria-label="Green island coastline">
    <div class="caption"><span>Bahamas - 5 days</span><span class="price">$1200</span></div>
  </div>

  <h2 class="abs region-title">South America</h2>
  <ul class="abs countries" style="list-style:none">
    <li>Brazil</li><li>Chile</li><li>Guyana</li>
    <li>Argentina</li><li class="active">Ecuador</li><li>Suriname</li>
    <li>Colombia</li><li>Bolivia</li><li>French Guiana</li>
    <li>Peru</li><li>Paraguay</li><li>Falkland Islands(UK)</li>
    <li>Venezuela</li><li>Uruguay</li><li></li>
  </ul>
  <article class="abs details">
    <h3>Details about cruises in Ecuador</h3>
    <p>Lorem ipsum dolor sit amet, consectetur adipiscing elit. Quid ergo aliud intellegetur nisi uti ne quae pars naturae neglegatur. Quare ad ea primum, si videtur; Piso igitur hoc modo, vir optimus tuique, ut scis, amantissimus. Plane idem, inquit, et maxima quidem, qua fieri nulla maior potest.</p>
  </article>

  <h2 class="abs partners-title" style="font-weight:400">Our reliable partners</h2>
  <svg class="abs arrow" style="left:37px" viewBox="0 0 12 12"><circle cx="6" cy="6" r="6" fill="#555"/><path d="M7.5 3.2L4 6l3.5 2.8z" fill="#fff"/></svg>
  <div class="abs partner" style="left:63px"><span></span></div>
  <div class="abs partner" style="left:183px"><span style="background:#e9c9c6"></span></div>
  <div class="abs partner" style="left:303px"><span class="round" style="background:#c8d4ea"></span></div>
  <div class="abs partner" style="left:423px"><span></span></div>
  <div class="abs partner" style="left:543px"><span style="background:#e9c9c6"></span></div>
  <svg class="abs arrow" style="left:645px" viewBox="0 0 12 12"><circle cx="6" cy="6" r="6" fill="#0b74b5"/><path d="M4.5 3.2L8 6l-3.5 2.8z" fill="#fff"/></svg>
</main>

<footer>
  <svg class="abs footer-bg" viewBox="0 0 694 260" preserveAspectRatio="none">
    <path d="M0 30C40 8 80 22 110 14S160 0 200 10 270 30 320 12 380 2 420 14 490 30 540 14 620 2 694 18V260H0Z" fill="#2aa0d6"/>
    <path d="M0 38C50 20 90 30 130 22S190 14 230 26 300 36 350 22 420 18 470 28 560 34 610 22 680 26 694 30V260H0Z" fill="#0b74b5"/>
  </svg>

  <div class="abs footer-col" style="left:50px">
    <h4>Pages</h4>
    <ul>
      <li class="current">About us</li><li>Contact us</li><li>FAQ</li>
      <li>Terms of service</li><li>Payment info</li><li>Reward points</li>
    </ul>
  </div>
  <div class="abs footer-col" style="left:189px">
    <h4>Cruise Info</h4>
    <ul><li>Cruise news</li><li>Visa</li><li>Honeymoon cruise</li><li>First time on a cruise</li></ul>
  </div>
  <div class="abs footer-col" style="left:340px">
    <h4>Newsletter</h4>
    <p style="line-height:9.5px;width:100px">Subscribe to the best cruise deals now!</p>
    <div class="news-input">Enter email</div>
    <div class="news-btn">Subscribe</div>
  </div>
  <div class="abs footer-col" style="left:492px">
    <h4>Contact us</h4>
    <p style="padding-left:3px">Bluefin Studio Ltd<br>Harbourline Plaza 18, Coral Rd<br>Port Lumen 4120 Marevia</p>
    <div class="contact-line" style="margin-top:15px">
      <svg width="9" height="9" viewBox="0 0 10 10"><path d="M2 0l2 2.5-1.2 1.3c.6 1.4 1.8 2.6 3.2 3.2L7.3 5.8 10 8 8.5 10C4 9.5.5 6 0 1.5z" fill="#fff"/></svg>
      <p>(555) 318-2046<br>(555) 318-2046</p>
    </div>
    <div class="contact-line" style="margin-top:3px">
      <svg width="10" height="7" viewBox="0 0 10 7"><rect width="10" height="7" fill="#fff"/><path d="M0 0l5 4 5-4" stroke="#0b74b5" fill="none"/></svg>
      <p style="line-height:8px">hello@wavecrest.example</p>
    </div>
  </div>

  <div class="abs footer-brand"><span class="mark"></span>Wavecrest</div>
  <p class="abs tagline">We are the most advanced cruise booking provider in China.</p>
  <p class="abs copyright">Copyright © wavecrest.example 2013. All rights reserved.</p>
</footer>

</body>
</html>
```